Bold Website Redesign for a Disruptive Training Brand

Brightmoor Labs is a bold, no-fluff sales & leadership training company powered by AI-driven practice and behavioral science. We’ve already built our website structure and copy in Craftly.io — now we need a designer to fully transform the visual design across all pages (Home, Approach, Programs, About, Contact).
We’re looking for a modern, memorable, high-performance aesthetic that blends human energy, science, and tech without feeling corporate or safe. Clean, bold typography, fluid layout, strong emotional hero moments, subtle motion, and imagery that mixes real people with abstract scientific/tech visuals.Because our clients are primarily North American, please ensure any human photography or AI-generated imagery reflects a North American business context and demographics (modern, diverse, and realistic).

Your job is visual redesign only — no coding required.
The final design must be practical to rebuild inside Craftly.io.

A full, detailed creative brief (plus logo files) is included in the uploaded files.
If you can bring a mix of edge, intelligence, and strong visual storytelling, we’d love to see your work.

Website is already built in Craftly.io at - https://brightmoor-website-tempdesign.craftly.app — structure is set, visuals need redesign.

```html
<!DOCTYPE html>
<html lang="en">
<head>
<meta charset="utf-8">
<title>Brightmoor Labs — Training that practices back</title>
<link rel="stylesheet" href="https://fonts.googleapis.com/css2?family=Space+Grotesk:wght@400;500;600;700&display=swap">
<style>
:root{
  --bg-deep:#03171c;
  --bg-teal:#0a4a4c;
  --glow:#2bd6c6;
  --blue-card:#3a62b2;
  --blue-card-2:#3e86c4;
  --navy:#062a52;
  --navy-2:#0b3c6a;
  --ink:#0a0f14;
  --white:#ffffff;
  --muted:#cfe0ee;
  --accent:#2d22f0;
  --link-blue:#2d5fc0;
  --cyan:#3fc3ee;
  --line:rgba(255,255,255,.18);
}
*{box-sizing:border-box;margin:0;padding:0}
html,body{width:1200px;height:767px;overflow:hidden}
body{
  font-family:"Space Grotesk",sans-serif;color:var(--white);
  background:
    radial-gradient(ellipse 60% 40% at 80% 40%,rgba(43,214,198,.35),transparent 70%),
    radial-gradient(ellipse 50% 30% at 10% 75%,rgba(43,214,198,.25),transparent 70%),
    linear-gradient(160deg,var(--bg-deep),var(--bg-teal) 55%,var(--bg-deep));
  position:relative;
}
.card{position:absolute;border-radius:16px;overflow:hidden}

/* Brand */
.brand{left:20px;top:20px;width:176px;height:383px;background:linear-gradient(180deg,var(--blue-card),var(--blue-card-2));padding:0 20px}
.brand-name{margin-top:118px;display:flex;align-items:center;gap:8px;justify-content:center;font-weight:600;font-size:15px;letter-spacing:.06em;text-transform:uppercase}
.brand-dot{width:12px;height:12px;border-radius:50%;background:var(--white);flex:none}
.brand-tag{margin-top:46px;font-size:16px;line-height:28px;font-weight:400}

/* Nav */
.nav{left:20px;top:423px;width:176px;height:324px;background:var(--ink);padding:42px 20px 0}
.nav ul{list-style:none}
.nav li{font-size:13px;font-weight:500;height:40px}
.nav li.active span{border-bottom:1px solid var(--white);padding-bottom:5px}
.btn-talk{position:absolute;left:20px;bottom:20px;width:137px;height:42px;border-radius:6px;background:var(--blue-card);display:flex;align-items:center;justify-content:center;font-size:15px;font-weight:500}

/* Hero */
.hero{left:217px;top:20px;width:766px;height:176px;border:1px solid var(--line);background:rgba(6,30,38,.55);padding:0 23px}
.hero h1{margin-top:37px;font-size:33px;font-weight:700;letter-spacing:-.005em}
.hero p{margin-top:28px;width:480px;font-size:11px;line-height:15px;color:var(--muted)}
.btn-how{position:absolute;right:20px;top:108px;width:169px;height:48px;border-radius:6px;background:var(--accent);display:flex;align-items:center;justify-content:center;font-size:15px;font-weight:600}

/* Chart */
.problem{left:217px;top:217px;width:570px;height:530px;background:linear-gradient(180deg,var(--navy),#04234a)}
.problem h2{position:absolute;left:25px;top:38px;width:510px;font-size:28px;line-height:38px;font-weight:700}
.problem p{position:absolute;left:25px;top:134px;width:470px;font-size:9px;line-height:12.5px;color:var(--muted)}
.problem svg{position:absolute;left:0;top:0}

/* Team */
.team{left:807px;top:214px;width:176px;height:316px;background:var(--white);color:var(--ink);padding:0 17px}
.team .arrow{margin-top:22px}
.team h3{margin-top:2px;font-size:28px;font-weight:700}
.avatar{margin-top:50px;width:50px;height:50px;border-radius:50%;background:radial-gradient(circle at 50% 40%,#c9a58f,#4a5a6e)}
.team .name{margin-top:8px;font-size:19px;font-weight:700;color:var(--link-blue)}
.team .role{font-size:7px;font-weight:500}
.team blockquote{margin-top:20px;font-size:10.5px;line-height:15px;color:#7d8590}

/* Steps */
.steps{left:1003px;top:20px;width:177px;height:510px;background:var(--ink);padding:0 20px;text-align:center}
.step{padding:33px 0 18px;border-bottom:1px solid rgba(255,255,255,.15)}
.step:first-child{padding-top:35px}
.step h4{font-size:22px;font-weight:700}
.step p{margin-top:10px;font-size:10.5px;line-height:15px;color:var(--muted)}
.steps .note{margin-top:16px;font-size:9px;line-height:12.5px;color:var(--cyan);font-weight:500}
.btn-more{position:absolute;left:20px;top:447px;width:137px;height:43px;border-radius:6px;background:var(--white);color:var(--link-blue);display:flex;align-items:center;justify-content:center;font-size:15px;font-weight:500}

/* Programs */
.programs{left:807px;top:550px;width:373px;height:197px;background:linear-gradient(180deg,#3a5fa8,#3a5ca6);padding:0 19px}
.programs h3{margin-top:26px;font-size:24px;font-weight:500}
.programs p{margin-top:10px;width:310px;font-size:9.5px;line-height:16.5px;color:var(--muted)}
.programs .cta{position:absolute;left:19px;bottom:31px;font-size:16px;font-weight:600}
.round-btn{position:absolute;right:16px;bottom:16px;width:57px;height:57px;border-radius:50%;background:var(--white);display:flex;align-items:center;justify-content:center}
</style>
</head>
<body>

<section class="card brand">
  <div class="brand-name"><span class="brand-dot"></span>Brightmoor Labs</div>
  <p class="brand-tag">AI-driven sustainment that builds mastery — so you don’t have to.</p>
</section>

<nav class="card nav">
  <ul>
    <li class="active"><span>Home</span></li>
    <li>Approach</li>
    <li>Programs</li>
    <li>About</li>
    <li>Contact</li>
  </ul>
  <div class="btn-talk">Let’s Talk</div>
</nav>

<section class="card hero">
  <h1>Training that practices back.</h1>
  <p>You’ll see measurable growth as your people turn insight into habit — automatically, sustainably, and without extra work for their leaders.</p>
  <div class="btn-how">See How we Do it</div>
</section>

<section class="card problem">
  <svg width="570" height="530" viewBox="0 0 684 636" aria-hidden="true">
    <defs>
      <linearGradient id="curveFill" x1="0" y1="0" x2="0" y2="1">
        <stop offset="0" stop-color="#3a6fc4" stop-opacity=".9"/>
        <stop offset="1" stop-color="#0b3a6e" stop-opacity=".5"/>
      </linearGradient>
    </defs>
    <path d="M30 288 C100 320 130 360 150 410 C170 450 200 450 250 448 C290 446 290 480 330 490 C370 500 390 495 430 500 C480 508 540 530 610 556 L610 558 L30 558 Z" fill="url(#curveFill)"/>
    <path d="M30 288 C100 320 130 360 150 410 C170 450 200 450 250 448 C290 446 290 480 330 490 C370 500 390 495 430 500 C480 508 540 530 610 556" fill="none" stroke="#3fc3ee" stroke-width="3.5"/>
    <path d="M30 288 C80 310 110 322 150 320 C190 318 200 305 240 316 C260 330 280 334 300 328 C330 340 360 340 400 332 C440 324 470 330 500 328 C540 324 580 302 610 286" fill="none" stroke="#fff" stroke-width="3.5"/>
    <g fill="#fff" font-family="Space Grotesk, sans-serif" font-size="13" font-weight="600">
      <text x="30" y="262">People forget</text><text x="30" y="280">fast.</text>
      <text x="370" y="366">Within a week,</text><text x="370" y="384">70% is gone</text>
      <text x="557" y="488">We built the</text><text x="557" y="506">fix in</text>
    </g>
    <g fill="#fff" font-family="Space Grotesk, sans-serif" font-size="22" font-weight="600">
      <text x="28" y="601">0</text><text x="140" y="601">2</text><text x="251" y="601">4</text>
      <text x="363" y="601">6</text><text x="474" y="601">8</text><text x="584" y="601">10</text>
    </g>
  </svg>
  <h2>The real problem isn’t your people — it’s the forgetting curve.</h2>
  <p>Within a week, most training disappears. Leaders are left guessing who’s using what they learned — and no one has time to fix it. We built Brightmoor Labs to make progress automatic, measurable, and real.</p>
</section>

<section class="card team">
  <svg class="arrow" width="19" height="19" viewBox="0 0 19 19" aria-hidden="true"><path d="M3 16 L16 3 M6 3 H16 V13" stroke="#0a0f14" stroke-width="2.4" fill="none"/></svg>
  <h3>Our Team</h3>
  <div class="avatar" role="img" aria-label="Portrait photo of the co-founder"></div>
  <div class="name">Mark Ellison</div>
  <div class="role">Co-Founder &amp; CEO</div>
  <blockquote>“Growth strategist and technologist, expert in scaling teams through insight and analytics.”</blockquote>
</section>

<aside class="card steps">
  <div class="step"><h4>1.Learn</h4><p>”It starts in the room — but it doesn’t end there.”</p></div>
  <div class="step"><h4>2.Certify</h4><p>”Practice happens automatically.”</p></div>
  <div class="step"><h4>3.Sustain</h4><p>”Learning becomes a habit — not a memory.”</p></div>
  <p class="note">A complete system for building lasting capability.</p>
  <div class="btn-more">Learn More</div>
</aside>

<section class="card programs">
  <h3>Adaptive Sales Mastery</h3>
  <p>Turn your sales team into a consistent, confident growth engine — one that practices, improves, and performs without you chasing follow-through.</p>
  <div class="cta">See our programs</div>
  <div class="round-btn"><svg width="20" height="20" viewBox="0 0 20 20" aria-hidden="true"><path d="M3 17 L17 3 M7 3 H17 V13" stroke="#2d5fc0" stroke-width="2.4" fill="none"/></svg></div>
</section>

</body>
</html>
```